Letterhead design for Dental Practice - Ashby Lane Dental Care

Letterhead for Private Dental Practice. To be used for all official correspondance and for printing treatment details on to be given to patients.

Target Market(s)

Private dental patients

Industry/Entity Type

Dental Clinic

Font styles to use
Other font styles liked:
• nexa-light

Colors
33a6d7
1c66ac
85abd2

Requirements
Must have
• info in the footer and header needs to be 3.5cm from upper/lower boader of paper, see photo in uploaded files
• info details:
• tel. 01632 947 305
• email info@ashbylanedc.co.uk
• ashbylanedentalcare.co.uk
• 17b Ashby Lane Eastmere Harwick HW4 7QT
• nexa-light font as in uploaded logo files
Should not have
• No funny tooth pictures

```html
<!DOCTYPE html>
<html lang="en">
<head>
<meta charset="utf-8">
<title>Ashby Lane Dental Care – Letterhead</title>
<link rel="stylesheet" href="https://fonts.googleapis.com/css2?family=Source+Sans+3:wght@400;700&family=Questrial&display=swap">
<style>
  :root {
    --paper: #ffffff;
    --ink: #3a3a3c;
    --ink-soft: #4d4d4f;
    --brand-blue: #33a6d7;
    --brand-navy: #1c66ac;
    --brand-mist: #85abd2;
    --watermark: #e7e8e9;
  }
  * { box-sizing: border-box; margin: 0; padding: 0; }
  html, body { width: 849px; height: 1200px; overflow: hidden; background: var(--paper); }
  .letterhead {
    position: relative;
    width: 849px;
    height: 1200px;
    background: var(--paper);
    font-family: "Source Sans 3", Arial, sans-serif;
    color: var(--ink);
  }
  .brand {
    position: absolute;
    left: 50px;
    top: 92px;
    display: flex;
    align-items: center;
    gap: 12px;
  }
  .brand-dot {
    width: 26px; height: 26px;
    border-radius: 50%;
    background: var(--brand-blue);
  }
  .brand-name {
    font-family: "Questrial", Arial, sans-serif;
    font-size: 27px;
    color: var(--brand-blue);
    letter-spacing: 0.2px;
  }
  .backdrop-ring {
    position: absolute;
    left: 256px;
    top: 460px;
  }
  .recipient {
    position: absolute;
    left: 50px;
    top: 276px;
    font-size: 16px;
    line-height: 21.3px;
    font-style: normal;
  }
  .recipient .recipient-name { font-weight: 700; }
  .body-copy {
    position: absolute;
    left: 50px;
    top: 426px;
    width: 634px;
    font-size: 16.2px;
    line-height: 21.4px;
    text-align: justify;
    hyphens: auto;
  }
  .body-copy p + p { margin-top: 21.4px; }
  .sign-off {
    position: absolute;
    left: 50px;
    top: 766px;
    font-size: 16px;
    line-height: 21.4px;
  }
  .contact {
    position: absolute;
    left: 54px;
    top: 1094px;
    font-family: "Questrial", Arial, sans-serif;
    font-size: 16.5px;
    line-height: 27px;
    color: var(--ink-soft);
    list-style: none;
  }
  .contact li { display: flex; align-items: center; gap: 8px; }
  .contact svg { width: 11px; height: 11px; flex: none; fill: var(--ink-soft); }
  .contact .link { color: var(--brand-blue); }
  .contact .web { display: inline-flex; align-items: center; gap: 4px; margin-left: 6px; }
</style>
</head>
<body>
<main class="letterhead">
  <header class="brand">
    <span class="brand-dot"></span>
    <span class="brand-name">Ashby Lane Dental Care</span>
  </header>

  <svg class="backdrop-ring" width="314" height="314" viewBox="0 0 314 314" aria-hidden="true">
    <circle cx="157" cy="157" r="144" fill="none" stroke="var(--watermark)" stroke-width="24"/>
  </svg>

  <address class="recipient">
    <div class="recipient-name">Name</div>
    <div>Title</div>
    <div>Address</div>
    <div>Postcode</div>
    <div>UK</div>
  </address>

  <section class="body-copy">
    <p>Lorem Ipsum is simply dummy vvvLorem ipsum dolor sit amet, consectetuer adipiscing elit, sed diam nonummy nibh euismod tincidunt ut laoreet dolore magna aliquam erat volutpat. Ut wisi enim ad minim veniam, quis nostrud exerci tation ullamcorper suscipit lobortis nisl ut aliquip ex ea commodo consequat. Duis autem vel eum iriure dolor in hendrerit in vulputate velit&nbsp; of Lorem Ipsum.</p>
    <p>Lorem ipsum dolor sit amet, consectetuer adipiscing elit, sed diam nonummy nibh euismod tincidunt ut laoreet dolore magna aliquam erat volutpat. Ut wisi enim ad minim veniam, quis nostrud exerci tation ullamcorper suscipit lobortis nisl ut aliquip ex ea commodo consequat. Duis autem vel eum iriure dolor in hendrerit in vulputate vel.</p>
    <p>Lorem ipsum dolor sit amet, consectetuer adipiscing elit.</p>
  </section>

  <div class="sign-off">
    <div>Name Here</div>
    <div>Signature</div>
  </div>

  <ul class="contact">
    <li>
      <svg viewBox="0 0 12 12" aria-hidden="true"><path d="M3 1 L5 3.5 L4 5 Q5 7 7 8 L8.5 7 L11 9 L9.5 11 Q4.5 10.5 1.5 4.5 Z"/></svg>
      <span>01632 947 305</span>
    </li>
    <li>
      <svg viewBox="0 0 12 12" aria-hidden="true"><rect x="1" y="3" width="10" height="6.5"/></svg>
      <span class="link">info@ashbylanedc.co.uk</span>
      <span class="web">
        <svg viewBox="0 0 12 12" aria-hidden="true"><circle cx="6" cy="6" r="4.5"/></svg>
        <span class="link">ashbylanedentalcare.co.uk</span>
      </span>
    </li>
    <li>
      <svg viewBox="0 0 12 12" aria-hidden="true"><path d="M6 0.5 A4 4 0 0 1 10 4.5 C10 7.5 6 11.5 6 11.5 C6 11.5 2 7.5 2 4.5 A4 4 0 0 1 6 0.5 Z M6 3 A1.5 1.5 0 1 0 6 6 A1.5 1.5 0 1 0 6 3 Z" fill-rule="evenodd"/></svg>
      <span class="link">17b Ashby Lane Eastmere Harwick HW4 7QT</span>
    </li>
  </ul>
</main>
</body>
</html>
```